Letterhead, envelope & business card design

We would like to refresh the look and feel of our business cards & letterheads.

Our company specialises in premium property.

We are looking for a unique minimalist design for our letterhead & business cards that project this.

I can send over examples of our current design to draw from, although Im looking for some one with creativity, yet focussed on a clean modern, minimalist design.
Updates

I have just uploaded our current letterhead.

We have just removed the 'swoosh' grey symbol, but would still like to keep some part of grey in the design if possible.

thanks in advance.

Just uploaded my details for business card.

Can we see examples with the light grey used as the secondary color?

thanks in advance.

Target Market(s)

We are a premium real estate agency & we want that message to be carried through our business cards & stationery.

Industry/Entity Type

Business

```html
<!DOCTYPE html>
<html lang="en">
<head>
<meta charset="utf-8">
<title>Harwood Estate Agents – Stationery</title>
<link rel="stylesheet" href="https://fonts.googleapis.com/css2?family=Roboto+Condensed:wght@400&display=swap">
<style>
  :root {
    --teal: #063d4f;
    --grey: #8c8c8c;
    --rule: #9fb3ba;
    --paper: #ffffff;
    --backdrop: #e6e5e1;
    --edge: #a8a8a8;
    --font: "Roboto Condensed", Arial, sans-serif;
  }
  * { margin: 0; padding: 0; box-sizing: border-box; }
  html, body {
    width: 1200px; height: 900px; overflow: hidden;
    background: var(--backdrop);
    font-family: var(--font);
  }
  .canvas { position: relative; width: 1200px; height: 900px; }

  /* Brand name */
  .brand { color: var(--teal); font-weight: 400; text-transform: uppercase; line-height: 1; }
  .brand__name { display: block; letter-spacing: 0.06em; }
  .brand__tag { display: block; letter-spacing: 0.32em; margin-top: 4px; }

  /* Letterhead */
  .letterhead {
    position: absolute; left: 70px; top: 40px;
    width: 584px; height: 826px;
    background: var(--paper);
    border-right: 8px solid var(--teal);
  }
  .letterhead .brand { position: absolute; left: 50px; top: 52px; }
  .letterhead .brand__name { font-size: 30px; }
  .letterhead .brand__tag { font-size: 9px; }
  .letterhead__contact {
    position: absolute; right: 16px; top: 24px;
    text-align: right; color: var(--grey);
    font-size: 8px; line-height: 1.35;
  }
  .letterhead__contact p + p { margin-top: 8px; }
  .letterhead__contact .legal { font-size: 6px; }

  /* Business cards */
  .card {
    position: absolute; left: 700px; width: 450px; height: 274px;
  }
  .card--front {
    top: 120px; background: var(--paper);
    border-bottom: 8px solid var(--teal);
  }
  .card--front .brand {
    position: absolute; left: 0; right: 0; top: 104px; text-align: center;
  }
  .card--front .brand__name { font-size: 40px; }
  .card--front .brand__tag { font-size: 11px; margin-top: 6px; }

  .card--back {
    top: 450px; background: var(--teal); color: #fff;
    border-bottom: 8px solid var(--edge);
  }
  .card__rule-v { position: absolute; left: 268px; top: 0; bottom: 0; width: 1px; background: var(--rule); }
  .card__rule-h { position: absolute; left: 268px; right: 0; top: 112px; height: 1px; background: var(--rule); }
  .card__person { position: absolute; left: 282px; top: 80px; }
  .card__person .name { font-size: 15px; }
  .card__person .role { font-size: 9px; margin-top: 2px; }
  .card__phones { position: absolute; left: 282px; top: 128px; font-size: 14px; line-height: 1.15; }
  .card__phones small { font-size: 9px; margin-right: 3px; }
  .card__address { position: absolute; left: 282px; top: 184px; font-size: 14px; line-height: 1.15; }
  .card__legal {
    position: absolute; right: 196px; top: 144px;
    text-align: right; font-size: 9px; line-height: 1.9;
  }
  .card__web {
    position: absolute; right: 196px; top: 212px;
    text-align: right; font-size: 14px; line-height: 1.15;
  }
</style>
</head>
<body>
<main class="canvas">

  <section class="letterhead" aria-label="Letterhead">
    <div class="brand">
      <span class="brand__name">Harwood</span>
      <span class="brand__tag">Estate Agents</span>
    </div>
    <div class="letterhead__contact">
      <p>t. 02 4310 5520<br>m. 0412 604 377</p>
      <p>58 Shore Street<br>Lakeview NSW 2261</p>
      <p>info@harwoodestates.com.au<br>www.harwoodestates.com.au</p>
      <p class="legal">ABN 41 208 775 390<br>Registered Valuer 022 481</p>
    </div>
  </section>

  <section class="card card--front" aria-label="Business card front">
    <div class="brand">
      <span class="brand__name">Harwood</span>
      <span class="brand__tag">Estate Agents</span>
    </div>
  </section>

  <section class="card card--back" aria-label="Business card back">
    <div class="card__rule-v"></div>
    <div class="card__rule-h"></div>
    <div class="card__person">
      <p class="name">Neil Harwood</p>
      <p class="role">Director</p>
    </div>
    <p class="card__phones"><small>t.</small>02 4310 5520<br><small>m.</small>0412 604 377</p>
    <p class="card__address">58 Shore Street<br>Lakeview NSW 2261</p>
    <p class="card__legal">ABN 41 208 775 390<br>Registered Valuer 022 481</p>
    <p class="card__web">info@harwoodestates.com.au<br>www.harwoodestates.com.au</p>
  </section>

</main>
</body>
</html>
```